Equine Psychotherapy and personal development flyer design

I am a therapist that works with horses to help people with issues like anxiety, depression, low self esteem, lack of confidence, loss of direction, spirituality and personal development. I work with adults, teenagers and children and one on one and in groups. I need the design to look professional, clear, engaging, warm and approachable.

Please use pink and navy colours and include the photos, logo and content I have uploaded. Please look at our website to get a clearer idea of what we do and to guide your design please make sure our website address is on the flyer www.torelin.com.au and our address is Gold Coast, QLD also my phone number 0418 352 906. Thank you for all of your submissions, creativity and work

Target Market(s)

professional people, families, schools

Industry/Entity Type

Work

Font styles to use
Script

Requirements
Must have
• A picture of a person or people with a horse, must be double sided
Nice to have
• Please use pink and navy colours and include the photos, logo and content I have uploaded. Please look at our website to get a clearer idea of what we do and to guide your design please make sure our website address is on the flyer www.torelin.com.au and our address is Gold Coast, QLD also my phone number 0418 352 906. Thank you for all of your submissions, creativity and work

```html
<!DOCTYPE html>
<html lang="en">
<head>
<meta charset="utf-8">
<title>Torelin Programs Flyer</title>
<link rel="stylesheet" href="https://fonts.googleapis.com/css2?family=Open+Sans:wght@400&family=PT+Sans:wght@400;700&family=PT+Serif:wght@400;700&display=swap">
<style>
  :root {
    --navy-top: #3a5a86;
    --navy: #12386e;
    --navy-deep: #0c2a58;
    --pink: #e8008a;
    --charcoal: #383838;
    --white: #ffffff;
    --ink: #1a1a1a;
    --rule: #8a8a8a;
  }
  * { box-sizing: border-box; margin: 0; padding: 0; }
  html, body { width: 1200px; height: 850px; overflow: hidden; background: var(--charcoal); }
  .flyer { position: relative; width: 1200px; height: 850px; background: var(--charcoal); font-family: "PT Sans", sans-serif; }

  .masthead {
    position: absolute; left: 0; top: 0; width: 1200px; height: 310px;
    background: linear-gradient(180deg, var(--navy-top) 0%, var(--navy) 32%, var(--navy-deep) 100%);
    border-bottom: 8px solid var(--pink);
    box-shadow: 0 6px 10px rgba(0,0,0,.45);
  }
  .brand { position: absolute; left: 60px; top: 120px; display: flex; align-items: center; gap: 18px; }
  .brand-mark { width: 64px; height: 64px; border-radius: 50%; background: var(--pink); flex: none; }
  .brand-name { font-family: "PT Sans", sans-serif; font-weight: 400; font-size: 42px; color: var(--white); line-height: 1; white-space: nowrap; }
  .contact { position: absolute; left: 60px; top: 212px; color: var(--white); font-size: 19px; line-height: 28px; }

  .intro {
    position: absolute; left: 517px; top: 33px; width: 646px;
    color: var(--white); font-family: "Open Sans", sans-serif; font-size: 18.4px; line-height: 32px;
  }
  .intro-line { display: block; white-space: nowrap; text-align: justify; text-align-last: justify; }
  .intro-line.last { text-align-last: left; }

  .programs { position: absolute; left: 78px; top: 335px; display: flex; gap: 13px; }
  .program { width: 264px; height: 326px; background: var(--white); position: relative; }
  .program-photo { position: absolute; left: 17px; top: 16px; width: 231px; height: 177px; }
  .photo-calm { background: linear-gradient(90deg, #6b3a22 0%, #7b4a2c 30%, #9aa56a 55%, #5b6d3c 100%); }
  .photo-care { background: radial-gradient(circle at 45% 60%, #7a3a1c 0%, #5c2a14 45%, #c9c3b4 80%); }
  .photo-lead { background: radial-gradient(circle at 45% 45%, #f1ede6 0%, #b7b1a6 40%, #3f3a34 100%); }
  .photo-flow { background: radial-gradient(circle at 60% 60%, #ffd35a 0%, #f39a1b 35%, #c5420c 70%, #3c1804 100%); }
  .program-title {
    position: absolute; left: 17px; top: 204px; width: 240px;
    font-size: 24.5px; font-weight: 700; line-height: 35px; color: var(--ink);
  }
  .program-title.compact { font-size: 23.5px; }
  .program-tag {
    position: absolute; left: 0; top: 286px; width: 100%; height: 40px;
    border-top: 1px solid var(--rule);
    padding: 9px 0 0 17px;
    font-family: "PT Serif", serif; font-weight: 700; font-size: 18px; color: var(--pink);
  }

  .newsletter {
    position: absolute; left: 78px; top: 678px; width: 1092px; height: 120px;
    background: var(--pink); box-shadow: 0 8px 10px rgba(0,0,0,.5);
  }
  .mail-icon { position: absolute; left: -48px; top: 19px; width: 88px; height: 88px; }
  .newsletter-head {
    position: absolute; left: 45px; top: 9px;
    font-family: "PT Serif", serif; font-size: 44.5px; color: var(--white); line-height: 52px; white-space: nowrap;
  }
  .newsletter-head strong { font-weight: 700; }
  .newsletter-line {
    position: absolute; left: 46px; top: 68px;
    font-family: "PT Serif", serif; font-size: 30px; color: var(--white); letter-spacing: 2.4px; white-space: nowrap;
  }
  .newsletter-line strong { color: var(--navy-deep); font-weight: 700; letter-spacing: 1px; }
</style>
</head>
<body>
<main class="flyer">
  <header class="masthead">
    <div class="brand">
      <span class="brand-mark" aria-hidden="true"></span>
      <span class="brand-name">Torelin Programs</span>
    </div>
    <p class="contact">0418 352 906 &middot; Gold Coast, QLD</p>
    <p class="intro">
      <span class="intro-line">Our programs provide skills for life. We offer individual therapy,</span>
      <span class="intro-line">group work, corporate learning and team building. We have</span>
      <span class="intro-line">programs in leadership, personal development and learning to assist</span>
      <span class="intro-line">you in living your life to its full potential. Maren and Lucy have a</span>
      <span class="intro-line">passion for teaching, health and personal development. Together they</span>
      <span class="intro-line">have over 30 years experience developing and teaching their diverse</span>
      <span class="intro-line">range of skills including horsemanship, equine assisted psychotherapy,</span>
      <span class="intro-line last">yoga, meditation, psychotherapy, art therapy and facilitating groups.</span>
    </p>
  </header>

  <section class="programs">
    <article class="program">
      <div class="program-photo photo-calm" role="img" aria-label="Woman standing calmly beside a brown horse"></div>
      <h2 class="program-title">Calm, Clear &amp;<br>Connected</h2>
      <p class="program-tag">Create a calmer life</p>
    </article>
    <article class="program">
      <div class="program-photo photo-care" role="img" aria-label="Hand resting on a brown horse's face wearing a halter"></div>
      <h2 class="program-title">Self-Care &amp;<br>Boundary Setting</h2>
      <p class="program-tag">Be clear on what you want</p>
    </article>
    <article class="program">
      <div class="program-photo photo-lead" role="img" aria-label="White horse galloping through dust"></div>
      <h2 class="program-title compact">Leadership &amp; Stepping<br>into your Power</h2>
      <p class="program-tag">Embrace your full ability</p>
    </article>
    <article class="program">
      <div class="program-photo photo-flow" role="img" aria-label="Silhouette of a person with raised arms against a sunset"></div>
      <h2 class="program-title">Creating Balance &amp;<br>Flow in your life</h2>
      <p class="program-tag">Tune into yourself</p>
    </article>
  </section>

  <aside class="newsletter">
    <svg class="mail-icon" viewBox="0 0 88 88" aria-hidden="true">
      <circle cx="44" cy="44" r="42" fill="#9a9a9a"/>
      <circle cx="44" cy="44" r="36" fill="#ffffff"/>
      <rect x="24" y="31" width="40" height="27" rx="2" fill="none" stroke="#111" stroke-width="3"/>
      <path d="M25 33 L44 47 L63 33 M25 57 L39 44 M63 57 L49 44" fill="none" stroke="#111" stroke-width="3"/>
    </svg>
    <p class="newsletter-head"><strong>Stay Connected!</strong> Sign up to our weekly <strong>Newsletter</strong></p>
    <p class="newsletter-line">Visit <strong>www.torelin.com.au</strong> and subscribe.</p>
  </aside>
</main>
</body>
</html>
```